Trade Show Booth Backdrop design

We need a design for our NEW Trade Show booth back drop and props. Booth will be a 10' x 20' flax canvas back drop with two fabric printed arches that extend over and out to the booths front edge. All specs, details, pictures, logos, colors will be provided. Looking for that WOW factor for this booth. Go to our website - yourshedhollow.com We want the same theme.
See pictures of our truck wraps / old booth back drop- a design like this promoting all our services.
We will work with whoever submits great new designs and help dial it in.

Target Market(s)

Homeowners

Industry/Entity Type

Home Improvment

Colors
FFC000
F8CF3A
FAE287
FDF2CF
FEFAEE

Requirements
Must have
• our logos, our mascot Dunby the troll, our Brand - We do concrete floor coatings, Cabinets, storage for garages.
Nice to have
• open for new ideas
Should not have
• open for ideas

```html
<!DOCTYPE html>
<html lang="en">
<head>
<meta charset="utf-8">
<title>Your Shed Hollow – Booth Backdrop</title>
<link href="https://fonts.googleapis.com/css2?family=Audiowide&family=Poppins:ital,wght@0,700;0,800;1,700;1,800&display=swap" rel="stylesheet">
<style>
  :root {
    --orange: #f0861a;
    --orange-deep: #d4740f;
    --black: #0b0b0b;
    --plate: #1c1c1c;
    --silver: #d9d9d9;
    --white: #ffffff;
    --grey: #5a5d5a;
    --skin: #f1b99a;
    --beard: #8d8f8d;
  }
  * { margin: 0; padding: 0; box-sizing: border-box; }
  html, body { width: 1200px; height: 600px; overflow: hidden; background: var(--black); }
  .backdrop {
    position: relative; width: 1200px; height: 600px; overflow: hidden;
    background: radial-gradient(ellipse at 60% 40%, var(--plate), var(--black) 75%);
    font-family: "Poppins", sans-serif; color: var(--white);
  }
  .shapes { position: absolute; inset: 0; }

  .mascot {
    position: absolute; left: 10px; top: 262px; width: 250px; height: 338px;
    border-radius: 45% 45% 12% 12%;
    background: radial-gradient(circle at 55% 32%, var(--skin), var(--beard) 55%, var(--orange) 88%);
  }

  .corner-claim {
    position: absolute; left: 18px; top: 132px; transform: rotate(-27deg); transform-origin: left top;
    font-weight: 800; color: var(--white); line-height: .92;
    -webkit-text-stroke: 2.5px var(--black); paint-order: stroke fill;
    text-shadow: 2px 2px 0 var(--black);
  }
  .corner-claim .pct { font-size: 58px; display: block; margin-left: 2px; }
  .corner-claim .kind { font-size: 47px; display: block; }

  .site-url {
    position: absolute; left: 104px; top: 222px; transform: rotate(-27deg); transform-origin: left top;
    font-weight: 700; font-size: 22px; letter-spacing: .5px; white-space: nowrap;
  }

  .brand { position: absolute; left: 405px; top: 40px; display: flex; align-items: center; gap: 24px; }
  .brand-mark { width: 160px; height: 160px; background: var(--orange); }
  .brand-name { font-family: "Audiowide", sans-serif; color: var(--orange); font-size: 66px; line-height: 1.05; }

  .services-title {
    position: absolute; left: 560px; top: 194px; width: 620px;
    font-family: "Audiowide", sans-serif; font-size: 28px; line-height: 1.3; text-align: center; font-style: italic;
  }
  .extras {
    position: absolute; left: 618px; top: 274px; white-space: nowrap;
    font-style: italic; font-weight: 700; font-size: 37px; color: var(--orange);
  }
  .promo { position: absolute; font-weight: 700; line-height: 1; }
  .promo-day { left: 795px; top: 328px; font-size: 66px; color: var(--white); }
  .promo-garage { left: 760px; top: 394px; font-size: 48px; color: var(--orange); }
  .promo-floors { left: 690px; top: 444px; font-size: 48px; color: var(--orange); }

  .tag {
    position: absolute; height: 45px; background: linear-gradient(var(--orange), var(--orange-deep));
    clip-path: polygon(0 0, 100% 0, 95% 100%, 0 100%);
    font-style: italic; font-weight: 800; font-size: 28px; white-space: nowrap;
    display: flex; align-items: center; color: var(--white);
    -webkit-text-stroke: 1.5px var(--black); paint-order: stroke fill; text-shadow: 2px 2px 0 var(--black);
  }
  .tag-garage { left: 240px; top: 277px; width: 250px; padding-left: 52px; }
  .tag-porches { left: 290px; top: 332px; width: 420px; padding-left: 54px; }
  .tag-office { left: 300px; top: 388px; width: 350px; padding-left: 32px; }
  .tag-warehouse { left: 300px; top: 444px; width: 362px; padding-left: 86px; }

  .social { position: absolute; top: 466px; left: 1102px; display: flex; gap: 12px; }
  .social span { width: 34px; height: 34px; background: var(--black); display: block; }

  .call-bar { position: absolute; left: 0; top: 522px; width: 1200px; height: 78px; background: var(--orange); }
  .mascot-front { z-index: 1; }
  .phone { position: absolute; left: 362px; top: 528px; display: flex; align-items: center; gap: 16px; z-index: 2; }
  .phone svg { width: 58px; height: 58px; }
  .phone-number {
    font-family: "Audiowide", sans-serif; font-style: italic; font-size: 68px; line-height: 1;
    color: var(--black); letter-spacing: 2px; white-space: nowrap;
    -webkit-text-stroke: 6px var(--white); paint-order: stroke fill;
  }
</style>
</head>
<body>
<div class="backdrop">
  <svg class="shapes" viewBox="0 0 1200 600" aria-hidden="true">
    <defs>
      <linearGradient id="steel" x1="0" y1="0" x2="1" y2="1">
        <stop offset="0" stop-color="#8a8a8a"/><stop offset=".5" stop-color="#ffffff"/><stop offset="1" stop-color="#7a7a7a"/>
      </linearGradient>
    </defs>
    <polygon points="0,0 500,0 0,255" fill="url(#steel)"/>
    <polygon points="0,0 370,0 0,222" fill="var(--orange)"/>
    <polygon points="870,505 1200,340 1200,505" fill="url(#steel)"/>
    <polygon points="960,505 1200,400 1200,505" fill="var(--orange)"/>
    <rect x="0" y="505" width="1200" height="12" fill="var(--grey)"/>
    <rect x="0" y="517" width="1200" height="5" fill="var(--silver)"/>
  </svg>

  <div class="call-bar"></div>
  <div class="mascot" role="img" aria-label="Dunby the troll mascot holding a paint roller"></div>

  <div class="corner-claim"><span class="pct">100%</span><span class="kind">POLYASPARTIC</span></div>
  <div class="site-url">www.yourshedhollow.com</div>

  <div class="brand">
    <div class="brand-mark"></div>
    <div class="brand-name">YOUR SHED<br>HOLLOW</div>
  </div>

  <div class="services-title">RESIDENTIAL AND COMMERCIAL<br>FLOOR COATINGS SERVICES</div>
  <div class="extras">QUALITY CABINETS &amp; MORE</div>

  <div class="promo promo-day">1 DAY</div>
  <div class="promo promo-garage">GARAGE</div>
  <div class="promo promo-floors">FLOORS</div>

  <div class="tag tag-garage">GARAGE</div>
  <div class="tag tag-porches">PORCHES &amp; PATIOS</div>
  <div class="tag tag-office">OFFICE FLOORS</div>
  <div class="tag tag-warehouse">WAREHOUSE</div>

  <div class="social"><span></span><span></span></div>

  <div class="phone">
    <svg viewBox="0 0 24 24" aria-hidden="true">
      <path d="M6.6 10.8c1.4 2.8 3.8 5.1 6.6 6.6l2.2-2.2c.3-.3.7-.4 1-.2 1.1.4 2.3.6 3.6.6.6 0 1 .4 1 1V20c0 .6-.4 1-1 1C10.6 21 3 13.4 3 4c0-.6.4-1 1-1h3.5c.6 0 1 .4 1 1 0 1.3.2 2.5.6 3.6.1.3 0 .7-.2 1z" fill="var(--black)" stroke="var(--white)" stroke-width="1.2"/>
    </svg>
    <span class="phone-number">(555) 014-2290</span>
  </div>
</div>
</body>
</html>
```